Re-design of veterinary clinic website *

For a future relaunch of our webpage, we would like to find a fresh design that still incorporates the spirit of our current one which can be found at http://dr-wenzlaff.de
We are a small business that appeals to locals but are known in a wide area for specialist services.
According to analytics data, most people rarely read through the full website but are using it to inform themselves about opening hours, Telephone numbers and location. Still, the website needs to offer enough content to be ranked positively by the Quandle algorithm.
Our logo is not part of the re-design but needs to be included in your proposal as is. It can be used a source of inspiration, just as the current design. Keep in mind, that the design will be used as the basis of a fluid webdesign for both mobile and desktop. Roughly 75% of our users are on mobile devices.
Target Market(s)
Locals
Industry/Entity Type
Veterinary
Number of Pages Required
1 page
Look and feel
Each slider illustrates characteristics of the customer's brand and the style your logo design should communicate.

```html
<!DOCTYPE html>
<html lang="en">
<head>
<meta charset="utf-8">
<title>Dr. med. vet. Konrad Wenzlaff – Veterinary Practice</title>
<link rel="stylesheet" href="https://fonts.googleapis.com/css2?family=Montserrat:wght@400;500;600;700;800&display=swap">
<style>
:root{
  --navy:#26408f;
  --navy-dark:#1f3478;
  --nav-active:#7fc3e6;
  --ink:#2b2b2b;
  --muted:#555;
  --pale:#f1f6fa;
  --footer:#161616;
  --white:#fff;
}
*{margin:0;padding:0;box-sizing:border-box}
html,body{width:1200px;height:2630px;overflow:hidden}
body{position:relative;font-family:'Montserrat',sans-serif;color:var(--ink);background:var(--white)}
.abs{position:absolute}

/* header */
.brand{left:250px;top:30px;display:flex;align-items:center;gap:14px}
.brand-mark{width:38px;height:38px;border-radius:50%;background:var(--navy)}
.brand-name{font-size:26px;font-weight:700;color:var(--navy);letter-spacing:1px}
.call{left:692px;top:18px;font-size:14px;font-weight:700;color:var(--navy)}
.call span{color:var(--ink);margin-left:8px}

.main-nav{left:0;top:117px;width:1200px;height:37px;background:var(--navy);display:flex;justify-content:center}
.main-nav ul{display:flex;list-style:none;margin-left:-20px}
.main-nav li{font-size:11.5px;font-weight:600;color:var(--white);padding:0 17px;line-height:37px;text-transform:uppercase}
.main-nav li.active{background:var(--nav-active);color:var(--navy-dark)}

/* hero */
.hero{left:0;top:154px;width:1200px;height:530px;overflow:hidden}
.hero-photo{position:absolute;inset:0;background:
  radial-gradient(ellipse 170px 260px at 1000px 300px,rgba(226,196,150,.95),rgba(226,196,150,0) 100%),
  radial-gradient(ellipse 120px 90px at 1010px 420px,rgba(214,120,120,.55),rgba(214,120,120,0) 100%),
  radial-gradient(ellipse 220px 330px at 650px 330px,rgba(255,255,255,.95),rgba(255,255,255,0) 100%),
  radial-gradient(ellipse 80px 90px at 600px 110px,rgba(214,168,140,.8),rgba(214,168,140,0) 100%),
  radial-gradient(ellipse 60px 70px at 560px 40px,rgba(150,95,60,.6),rgba(150,95,60,0) 100%),
  linear-gradient(90deg,#e3e9ec 0%,#d6dfe4 30%,#e9eef0 50%,#dfe5e4 70%,#d5d3cb 100%)}
.hero-title{left:133px;top:150px;font-size:37px;font-weight:800;line-height:46px;color:#1e1e1e;text-transform:uppercase}
.hero-text{left:133px;top:254px;font-size:14.5px;font-weight:500;line-height:22px;color:#1e1e1e;width:390px}
.btn{left:133px;top:318px;width:162px;height:42px;border-radius:21px;background:var(--navy);color:var(--white);font-size:12px;font-weight:700;text-align:center;line-height:42px;text-transform:uppercase}
.slide-arrow{top:194px;width:32px;height:32px;border-radius:50%;background:rgba(90,90,90,.55);display:flex;align-items:center;justify-content:center}
.hero-wave{left:0;bottom:0;width:1200px;height:110px}

/* section headings */
.section-title{left:0;width:1200px;text-align:center;font-size:25px;font-weight:400;letter-spacing:.5px;text-transform:uppercase;color:#222}
.section-title b{font-weight:700}
.lead{left:0;width:1200px;text-align:center;font-size:11.5px;line-height:23px;color:var(--muted)}

.tile{top:852px;width:264px;height:185px;border:1px solid #ddd}
.body-copy{left:228px;top:1074px;width:746px;text-align:center;font-size:11px;line-height:21.5px;color:var(--muted)}

/* services */
.services{left:0;top:1207px;width:1200px;height:562px;background:var(--pale)}
.service-photo{width:248px;height:248px;border-radius:50%;border:8px solid #dbe3f0}
.service{width:300px;text-align:center}
.service h3{font-size:14px;font-weight:600;color:#333;line-height:19px;margin-bottom:6px}
.service p{font-size:11px;line-height:18px;color:#444}

/* team */
.member-photo{top:1898px;width:174px;height:188px}
.member-name{top:2098px;width:230px;text-align:center;font-size:12.5px;font-weight:600;color:#222;text-transform:uppercase}

/* footer */
.footer-wave{left:0;top:2170px;width:1200px;height:110px}
.footer{left:0;top:2266px;width:1200px;height:364px;background:var(--footer);color:var(--white)}
.footer h4{font-size:14px;font-weight:600;text-transform:uppercase;letter-spacing:.3px}
.contact-row{display:flex;gap:14px;font-size:11px;line-height:21px;color:#ddd}
.phone-row{display:flex;gap:14px;align-items:center;font-size:14px;font-weight:600}
.hours{font-size:11px;color:#ddd;border-collapse:collapse}
.hours td{height:36px;padding-right:22px}
.map{left:753px;top:61px;width:314px;height:208px;border:1px solid #ccc;background:
  radial-gradient(ellipse 90px 60px at 110px 90px,rgba(170,205,150,.7),rgba(170,205,150,0) 100%),
  radial-gradient(ellipse 80px 110px at 230px 110px,rgba(245,222,160,.8),rgba(245,222,160,0) 100%),
  radial-gradient(ellipse 60px 40px at 60px 170px,rgba(190,210,230,.7),rgba(190,210,230,0) 100%),
  linear-gradient(135deg,#eef0ea,#e4e7e1 55%,#f1ede2)}
.copyright{left:0;top:320px;width:1200px;text-align:center;font-size:10px;color:#bbb}
</style>
</head>
<body>

<header>
  <div class="abs brand"><span class="brand-mark"></span><span class="brand-name">Konrad Wenzlaff</span></div>
  <div class="abs call">Call Us Today : <span>207-555-0148</span></div>
</header>

<nav class="abs main-nav">
  <ul>
    <li class="active">Hauptseite</li>
    <li>Praxis</li>
    <li>Team</li>
    <li>Sprechzeiten</li>
    <li>Leistungen</li>
    <li>Kontakt / Anfahrt</li>
  </ul>
</nav>

<section class="abs hero">
  <div class="hero-photo" role="img" aria-label="Smiling veterinarian with stethoscope beside a golden retriever"></div>
  <h1 class="abs hero-title">Providing special care<br>for your pets</h1>
  <p class="abs hero-text">Your pet is in good hands with us! Let your favorite get the best care in our center.</p>
  <div class="abs btn">Read more</div>
  <div class="abs slide-arrow" style="left:58px"><svg width="10" height="10" viewBox="0 0 10 10"><path d="M6.5 1.5 3 5l3.5 3.5" fill="none" stroke="#fff" stroke-width="1.6"/></svg></div>
  <div class="abs slide-arrow" style="left:1098px"><svg width="10" height="10" viewBox="0 0 10 10"><path d="M3.5 1.5 7 5 3.5 8.5" fill="none" stroke="#fff" stroke-width="1.6"/></svg></div>
  <svg class="abs hero-wave" viewBox="0 0 1200 110" preserveAspectRatio="none">
    <path d="M0 40 C200 70 380 95 560 70 C760 40 900 20 1200 90 L1200 110 L0 110Z" fill="#b8c3de" opacity=".75"/>
    <path d="M0 52 C200 82 380 105 560 80 C760 52 900 34 1200 100 L1200 110 L0 110Z" fill="#fff"/>
  </svg>
</section>

<section>
  <h2 class="abs section-title" style="top:733px">Welcome to <b>Konrad Wenzlaff!</b></h2>
  <p class="abs lead" style="top:774px">Welcome to the homepage of the veterinary practice of Dr. med. Konrad Wenzlaff. My team and I have put together information about<br>the practice and information for patients.</p>
  <div class="abs tile" style="left:156px;background:
    radial-gradient(ellipse 70px 60px at 150px 130px,rgba(214,160,80,.9),rgba(214,160,80,0) 100%),
    radial-gradient(ellipse 70px 100px at 60px 90px,rgba(255,255,255,.95),rgba(255,255,255,0) 100%),
    radial-gradient(ellipse 60px 90px at 215px 90px,rgba(250,248,244,.95),rgba(250,248,244,0) 100%),
    linear-gradient(135deg,#dfe7ee,#e8ebef 60%,#cfd9e4)" role="img" aria-label="Two veterinarians examining a golden puppy"></div>
  <div class="abs tile" style="left:463px;background:
    radial-gradient(ellipse 50px 65px at 80px 120px,rgba(70,70,75,.75),rgba(70,70,75,0) 100%),
    radial-gradient(ellipse 80px 90px at 190px 110px,rgba(255,255,255,.95),rgba(255,255,255,0) 100%),
    radial-gradient(ellipse 40px 40px at 170px 40px,rgba(120,80,55,.55),rgba(120,80,55,0) 100%),
    linear-gradient(135deg,#b9d4a8,#dfe5e2 55%,#eef1f3)" role="img" aria-label="Veterinarian listening to a cat with a stethoscope"></div>
  <div class="abs tile" style="left:779px;background:
    radial-gradient(ellipse 55px 60px at 70px 95px,rgba(160,150,150,.7),rgba(160,150,150,0) 100%),
    radial-gradient(ellipse 45px 40px at 200px 60px,rgba(215,150,90,.75),rgba(215,150,90,0) 100%),
    radial-gradient(ellipse 90px 45px at 170px 140px,rgba(180,110,60,.75),rgba(180,110,60,0) 100%),
    linear-gradient(#fbfbfb,#f1f0ee)" role="img" aria-label="Rabbit, hamster and guinea pigs"></div>
  <p class="abs body-copy">In addition, you can arrange appointments outside of this time with us. This is particularly recommended for predictable examinations or treatments such as vaccinations or dressings, more extensive examinations, detailed counseling sessions or even for particularly anxious or difficult to handle animals. Please let us know at the time of appointment on the phone with just how many animals you want to come and what we can do for you, so that we can take this into account in the scheduling.</p>
</section>

<section class="abs services">
  <h2 class="abs section-title" style="top:34px">Our <b>Veterinary Services</b></h2>
  <p class="abs lead" style="top:76px">The practice offers a comprehensive range based on a long-term exclusive experience in<br>small animal medicine</p>
  <div class="abs service-photo" style="left:138px;top:136px;background:
    radial-gradient(ellipse 80px 60px at 160px 130px,rgba(185,110,50,.95),rgba(185,110,50,0) 100%),
    radial-gradient(ellipse 40px 45px at 70px 150px,rgba(60,60,65,.7),rgba(60,60,65,0) 100%),
    linear-gradient(#f7f3ee,#f0e7dc 60%,#e9ddcf)" role="img" aria-label="Cat and dog resting together"></div>
  <div class="abs service-photo" style="left:470px;top:158px;background:
    radial-gradient(ellipse 70px 50px at 140px 80px,rgba(255,255,255,.95),rgba(255,255,255,0) 100%),
    radial-gradient(ellipse 60px 60px at 80px 110px,rgba(160,95,50,.85),rgba(160,95,50,0) 100%),
    radial-gradient(ellipse 90px 50px at 110px 200px,rgba(70,60,55,.7),rgba(70,60,55,0) 100%),
    linear-gradient(#6fa6dc,#a9c9ea 60%,#c7d7e6)" role="img" aria-label="Dog looking out of a car window"></div>
  <div class="abs service-photo" style="left:787px;top:136px;background:
    radial-gradient(ellipse 60px 80px at 120px 100px,rgba(30,32,36,.95),rgba(30,32,36,0) 100%),
    radial-gradient(ellipse 80px 40px at 140px 190px,rgba(240,240,245,.9),rgba(240,240,245,0) 100%),
    linear-gradient(135deg,#5aa6dc,#8cc6ea 60%,#d7e8f3)" role="img" aria-label="Gloved hands holding an endoscope"></div>
  <div class="abs service" style="left:112px;top:401px"><h3>Main Treatments</h3><p>Our main treatments are in internal medicine<br>and surgery of dogs and cats.</p></div>
  <div class="abs service" style="left:444px;top:419px"><h3>Special counseling<br>and support services</h3><p>Die Praxis bietet folgende besondere<br>Betreuungs- und Beratungsleistungen:</p></div>
  <div class="abs service" style="left:767px;top:401px"><h3>Medical Institutions</h3><p>Among other things, the practice has the fol-<br>lowing medical facilities for examination and<br>treatment</p></div>
</section>

<section>
  <h2 class="abs section-title" style="top:1823px">Our <b>Team Services</b></h2>
  <div class="abs member-photo" style="left:142px;background:
    radial-gradient(ellipse 55px 70px at 85px 80px,rgba(215,165,135,.9),rgba(215,165,135,0) 100%),
    radial-gradient(ellipse 90px 50px at 100px 185px,rgba(225,225,220,.95),rgba(225,225,220,0) 100%),
    linear-gradient(160deg,#e6e6e6,#cfcfcf)" role="img" aria-label="Portrait of Dr. Konrad Wenzlaff"></div>
  <div class="abs member-photo" style="left:391px;background:
    radial-gradient(ellipse 35px 45px at 85px 55px,rgba(225,180,150,.9),rgba(225,180,150,0) 100%),
    radial-gradient(ellipse 90px 60px at 85px 170px,rgba(150,40,65,.95),rgba(150,40,65,0) 100%),
    radial-gradient(ellipse 35px 30px at 95px 160px,rgba(90,60,40,.8),rgba(90,60,40,0) 100%),
    linear-gradient(#e9e9e9,#d6d6d6)" role="img" aria-label="Portrait of Dr. Sabine Kohlmann holding a puppy"></div>
  <div class="abs member-photo" style="left:637px;background:
    radial-gradient(ellipse 35px 45px at 87px 65px,rgba(225,180,150,.9),rgba(225,180,150,0) 100%),
    radial-gradient(ellipse 95px 55px at 87px 175px,rgba(140,35,60,.95),rgba(140,35,60,0) 100%),
    linear-gradient(#4f6a34,#7f9350)" role="img" aria-label="Portrait of Miriam Falk"></div>
  <div class="abs member-photo" style="left:884px;background:
    radial-gradient(ellipse 35px 45px at 80px 55px,rgba(235,205,160,.9),rgba(235,205,160,0) 100%),
    radial-gradient(ellipse 90px 55px at 85px 175px,rgba(190,70,110,.9),rgba(190,70,110,0) 100%),
    radial-gradient(ellipse 30px 30px at 95px 150px,rgba(120,85,60,.8),rgba(120,85,60,0) 100%),
    linear-gradient(#6d9a48,#9ab86a)" role="img" aria-label="Portrait of Lena Hartwig holding a kitten"></div>
  <div class="abs member-name" style="left:114px">Dr. Konrad Wenzlaff</div>
  <div class="abs member-name" style="left:363px">Dr. Sabine Kohlmann</div>
  <div class="abs member-name" style="left:609px">Miriam Falk</div>
  <div class="abs member-name" style="left:856px">Lena Hartwig</div>
</section>

<svg class="abs footer-wave" viewBox="0 0 1200 110" preserveAspectRatio="none">
  <path d="M0 90 C250 20 420 0 640 45 C850 90 1000 70 1200 10 L1200 110 L0 110Z" fill="var(--navy)"/>
  <path d="M0 104 C250 34 420 14 640 59 C850 104 1000 84 1200 24 L1200 110 L0 110Z" fill="var(--footer)"/>
</svg>

<footer class="abs footer">
  <h4 class="abs" style="left:136px;top:58px">Contact us</h4>
  <div class="abs contact-row" style="left:140px;top:90px">
    <svg width="14" height="12" viewBox="0 0 14 12" style="margin-top:4px"><path d="M7 0 0 6h2v6h4V8h2v4h4V6h2z" fill="#fff"/></svg>
    <div>Dr. med. vet. Konrad Wenzlaff<br>Veterinarian for small animals<br>Birkenallee 12<br>14163 Berlin (Zehlendorf)</div>
  </div>
  <div class="abs phone-row" style="left:140px;top:206px">
    <svg width="13" height="13" viewBox="0 0 24 24"><path d="M6.6 10.8a15 15 0 0 0 6.6 6.6l2.2-2.2a1 1 0 0 1 1-.25 11.4 11.4 0 0 0 3.6.57 1 1 0 0 1 1 1V20a1 1 0 0 1-1 1A17 17 0 0 1 3 4a1 1 0 0 1 1-1h3.5a1 1 0 0 1 1 1c0 1.25.2 2.45.57 3.570a1 1 0 0 1-.25 1z" fill="#fff"/></svg>
    030/555 01 22
  </div>
  <div class="abs phone-row" style="left:140px;top:244px">
    <svg width="14" height="13" viewBox="0 0 14 13"><rect x="0" y="4" width="14" height="9" rx="1" fill="#fff"/><rect x="3" y="0" width="8" height="5" fill="#fff"/><rect x="3" y="7" width="8" height="4" fill="#161616"/></svg>
    030/555 01 23
  </div>

  <h4 class="abs" style="left:389px;top:58px">Office hours without appointment</h4>
  <table class="abs hours" style="left:391px;top:86px">
    <tr><td>Mon - Wed</td><td>09.30 - 11.00</td><td>16.00 - 19.00</td></tr>
    <tr><td>Thursday</td><td></td><td>16.00 - 19.00</td></tr>
    <tr><td>Friday</td><td>09.30 - 11.00</td><td>16.00 - 19.00</td></tr>
    <tr><td>Saturday</td><td>09.30 - 11.00</td><td></td></tr>
  </table>

  <div class="abs map" role="img" aria-label="Quandle street map showing the practice location in Berlin Zehlendorf"></div>

  <p class="abs copyright">Copyright © 2019 dr-wenzlaff.de. All Rights Reserved</p>
</footer>

</body>
</html>
```